Business Card for By Karel Voss

Looking to have a business card designed for my lifestyle and fitness company. My company offers personal training, online programming and nutrition advice based out of London, United Kingdom.

I'd like to see modern, sleek designs, focusing on black, matte black or matte grey. Design doesn't need to be overly descriptive as this will also be used as a personal business card. I've included my logo.

Please note that my company is no longer called "Fitness by Karel Voss" but instead "By Karel Voss", this is because of my other ventures. Therefore please don't use the "fitness by karel voss" text.

information about my company can be found at www.bykarelvoss.com

Company is also based out of London (United Kingdom) & Sydney (Australia) this could be reflected on the card.

Industry/Entity Type

Business

Contact Information for Business Card

Karel Voss
+44 7382 615027
karel@bykarelvoss.com
www.bykarelvoss.com

Font styles to use
Sans Serif

Requirements
Must have
• All contact details and inclusion of my logo.

```html
<!DOCTYPE html>
<html lang="en">
<head>
<meta charset="UTF-8">
<title>By Karel Voss — Business Card</title>
<link href="https://fonts.googleapis.com/css2?family=Exo+2:wght@400;700&display=swap" rel="stylesheet">
<style>
  :root {
    --backdrop: #141414;
    --card: #1e1e20;
    --ink: #f4f4f4;
    --ink-soft: #d9d9d9;
    --rule: #8a8a8c;
  }
  * { margin: 0; padding: 0; box-sizing: border-box; }
  html, body {
    width: 1200px;
    height: 1000px;
    overflow: hidden;
    background: var(--backdrop);
    font-family: "Exo 2", sans-serif;
  }
  .canvas {
    width: 1200px;
    height: 1000px;
    display: flex;
    align-items: center;
    justify-content: center;
    gap: 60px;
  }
  .card {
    width: 510px;
    height: 292px;
    background: var(--card);
    position: relative;
    box-shadow: 0 10px 30px rgba(0,0,0,.5);
  }
  /* Front */
  .card-front {
    display: flex;
    align-items: center;
    justify-content: center;
  }
  .brand {
    display: flex;
    align-items: center;
    gap: 14px;
  }
  .brand-mark {
    width: 18px;
    height: 18px;
    border-radius: 50%;
    background: var(--ink);
  }
  .brand-name {
    color: var(--ink);
    font-weight: 700;
    font-size: 34px;
    letter-spacing: 1px;
    text-transform: uppercase;
  }
  /* Back */
  .card-back {
    display: flex;
    align-items: center;
    padding: 0 40px;
  }
  .holder-name {
    color: var(--ink);
    font-weight: 700;
    font-size: 26px;
    letter-spacing: .5px;
    width: 200px;
  }
  .divider {
    width: 1px;
    height: 90px;
    background: var(--rule);
    margin: 0 34px 0 10px;
  }
  .contact-list {
    list-style: none;
    color: var(--ink-soft);
    font-size: 15px;
    line-height: 1.45;
    letter-spacing: .4px;
  }
</style>
</head>
<body>
  <main class="canvas">
    <section class="card card-front" aria-label="Business card front">
      <div class="brand">
        <span class="brand-mark"></span>
        <span class="brand-name">By Karel Voss</span>
      </div>
    </section>
    <section class="card card-back" aria-label="Business card back">
      <h1 class="holder-name">Karel Voss</h1>
      <span class="divider"></span>
      <ul class="contact-list">
        <li>+44 7382 615027</li>
        <li>karel@bykarelvoss.com</li>
        <li>www.bykarelvoss.com</li>
      </ul>
    </section>
  </main>
</body>
</html>
```